TK Drafting

Simple Design - Logo is done (from this site). Logo on one side - Back Side an image or outline of a house blue print - My name, phone, email, website url. Prefer the traditional Architectural style of letters -

Target Market(s)

Customers who need a floor plan redesigned for renovations or realtors who want a floor plan for marketing their listings

Industry/Entity Type

Architecture

Contact Information for Business Card

Colby Faust - Name
415-362-8840 - Phone
tkdraftingco@mailpost.example
www.tkdraftingco.example

Font styles to use
Other font styles liked:
• Architecture writing -

Colors
0555a3
3276b5
85acd3

Requirements
Must have
• Logo that is attached. I like an indigo blue color for the background or a royal blue - gray logo OR - white and clean with the logo on one side and the same color gray lettering on the other side
Nice to have
• some sort of image that shows a residential blue print. It may not be possible on this small of a card though.
Should not have
• Nothing cartoonish.

```html
<!DOCTYPE html>
<html lang="en">
<head>
<meta charset="utf-8">
<title>TK Drafting — Business Card</title>
<link href="https://fonts.googleapis.com/css2?family=Arimo:wght@400;700&display=swap" rel="stylesheet">
<style>
  :root {
    --backdrop: #c9c9c9;
    --front-blue: #4585c3;
    --front-blue-deep: #3a79b8;
    --back-black: #1f1f1f;
    --back-black-soft: #2a2a2a;
    --accent-blue: #3276b5;
    --logo-gray: #b5b6bd;
    --text-white: #ffffff;
    --text-light: #e8e8e8;
  }
  * { box-sizing: border-box; margin: 0; padding: 0; }
  html, body {
    width: 1200px; height: 900px; overflow: hidden;
    background: var(--backdrop);
    font-family: "Arimo", Arial, sans-serif;
  }
  .canvas { position: relative; width: 1200px; height: 900px; }

  .card {
    position: absolute;
    width: 560px; height: 320px;
    border-radius: 26px;
    overflow: hidden;
    box-shadow: 0 10px 24px rgba(0,0,0,0.28);
  }

  /* Front side */
  .card-front { left: 80px; top: 100px; background: var(--front-blue); }
  .front-sketch {
    position: absolute; inset: 0;
    background: radial-gradient(ellipse at 50% 55%, var(--front-blue) 0%, var(--front-blue-deep) 100%);
  }
  .front-wordmark {
    position: absolute; left: 0; right: 0; top: 50%;
    transform: translateY(-50%);
    display: flex; align-items: center; justify-content: center; gap: 16px;
  }
  .front-wordmark .mark-square {
    width: 22px; height: 22px; background: var(--text-white);
  }
  .front-wordmark .brand-name {
    color: var(--text-white); font-weight: 400;
    font-size: 40px; letter-spacing: 6px; text-transform: uppercase;
  }

  /* Back side */
  .card-back { left: 560px; top: 480px; background: var(--back-black); }
  .back-sheen {
    position: absolute; left: 0; top: 0; width: 100%; height: 55%;
    background: linear-gradient(170deg, var(--back-black-soft) 0%, var(--back-black) 70%);
  }
  .back-wordmark {
    position: absolute; right: 36px; top: 52px;
    display: flex; align-items: center; gap: 12px;
  }
  .back-wordmark .mark-square { width: 16px; height: 16px; background: var(--logo-gray); }
  .back-wordmark .brand-name {
    color: var(--logo-gray); font-weight: 400;
    font-size: 28px; letter-spacing: 5px; text-transform: uppercase;
  }
  .back-rule {
    position: absolute; left: 36px; right: 36px; top: 120px;
    height: 2px; background: var(--accent-blue);
  }
  .contact-block { position: absolute; left: 36px; bottom: 34px; }
  .contact-name {
    color: var(--accent-blue); font-weight: 700;
    font-size: 24px; letter-spacing: 0.5px; text-transform: uppercase;
    padding-bottom: 8px; border-bottom: 2px solid var(--accent-blue);
    display: inline-block; min-width: 230px;
  }
  .contact-list { list-style: none; margin-top: 10px; }
  .contact-list li {
    display: flex; align-items: center; gap: 10px;
    color: var(--text-light); font-size: 16px; line-height: 24px;
  }
  .contact-list svg { width: 15px; height: 15px; flex: none; }
</style>
</head>
<body>
<main class="canvas">
  <section class="card card-front">
    <div class="front-sketch" role="img" aria-label="Faint pencil sketch of a residential interior drawn in light blue lines"></div>
    <div class="front-wordmark">
      <span class="mark-square"></span>
      <span class="brand-name">TK Drafting</span>
    </div>
  </section>

  <section class="card card-back">
    <div class="back-sheen"></div>
    <div class="back-wordmark">
      <span class="mark-square"></span>
      <span class="brand-name">TK Drafting</span>
    </div>
    <div class="back-rule"></div>
    <div class="contact-block">
      <div class="contact-name">Colby Faust</div>
      <ul class="contact-list">
        <li>
          <svg viewBox="0 0 16 16" aria-hidden="true"><path d="M4 1.5l2.5 3-1.5 1.5c.8 1.8 2.2 3.2 4 4l1.5-1.5 3 2.5-1.5 2.5C7 13.5 2.5 9 1.5 4z" fill="var(--accent-blue)"/></svg>
          415-362-8840
        </li>
        <li>
          <svg viewBox="0 0 16 16" aria-hidden="true"><rect x="1" y="3" width="14" height="10" fill="var(--accent-blue)"/><path d="M1 3l7 6 7-6" fill="none" stroke="var(--back-black)" stroke-width="1.4"/></svg>
          tkdraftingco@mailpost.example
        </li>
        <li>
          <svg viewBox="0 0 16 16" aria-hidden="true"><g fill="none" stroke="var(--accent-blue)" stroke-width="1.4"><circle cx="8" cy="8" r="6.5"/><ellipse cx="8" cy="8" rx="2.8" ry="6.5"/><path d="M1.5 8h13M2.5 4.8h11M2.5 11.2h11"/></g></svg>
          www.tkdraftingco.example
        </li>
      </ul>
    </div>
  </section>
</main>
</body>
</html>
```